Business cards design on a high standard

We advise clients on insurance and financial matters, since these clients pay for our advice, the design should have a high standard. Our logo should be included. From the colors we are open for everything.

Colors

Designer to choose colors to be used in the design.

```html
<!DOCTYPE html>
<html lang="en">
<head>
<meta charset="utf-8">
<title>Alpine Counsel business cards</title>
<link href="https://fonts.googleapis.com/css2?family=Montserrat:wght@600;700&family=Roboto:wght@400&display=swap" rel="stylesheet">
<style>
  :root {
    --brand-red: #e30613;
    --ink-grey: #8d8d8f;
    --arc-grey: #a7a8aa;
    --paper: #ffffff;
    --text-dark: #333333;
    --backdrop: #5a5a5c;
  }
  * { margin: 0; padding: 0; box-sizing: border-box; }
  html, body { width: 1200px; height: 960px; overflow: hidden; }
  body {
    background: var(--backdrop);
    position: relative;
    font-family: "Roboto", Arial, sans-serif;
  }
  .card {
    position: absolute;
    left: 250px;
    width: 700px;
    height: 400px;
    overflow: hidden;
    box-shadow: 0 6px 18px rgba(0,0,0,0.35);
  }
  .card--front { top: 60px; background: var(--brand-red); }
  .card--back { top: 500px; background: var(--paper); }
  .card__shape { position: absolute; inset: 0; }

  .wordmark {
    position: absolute;
    display: flex;
    align-items: center;
    gap: 12px;
    font-family: "Montserrat", Arial, sans-serif;
    font-weight: 700;
    letter-spacing: 2px;
    text-transform: uppercase;
    white-space: nowrap;
  }
  .wordmark__dot { border-radius: 50%; flex: none; }
  .card--front .wordmark {
    left: 50%; top: 50%;
    transform: translate(-50%, -50%);
    font-size: 44px;
    color: var(--paper);
  }
  .card--front .wordmark__dot { width: 26px; height: 26px; background: var(--paper); }
  .card--back .wordmark {
    right: 54px; top: 70px;
    font-size: 30px;
    color: var(--brand-red);
  }
  .card--back .wordmark__dot { width: 18px; height: 18px; background: var(--brand-red); }

  .holder {
    position: absolute;
    left: 70px;
    bottom: 34px;
  }
  .holder__name {
    font-family: "Montserrat", Arial, sans-serif;
    font-weight: 700;
    font-size: 24px;
    color: var(--brand-red);
    text-transform: uppercase;
    letter-spacing: 0.5px;
  }
  .holder__role {
    font-family: "Montserrat", Arial, sans-serif;
    font-weight: 700;
    font-size: 15px;
    color: var(--ink-grey);
    text-transform: uppercase;
    letter-spacing: 0.5px;
    margin-bottom: 18px;
  }
  .contact { list-style: none; }
  .contact__item {
    display: flex;
    align-items: center;
    gap: 10px;
    font-size: 15px;
    color: var(--text-dark);
    line-height: 22px;
  }
  .contact__icon { width: 13px; height: 13px; flex: none; }
</style>
</head>
<body>

<section class="card card--front" aria-label="Card front">
  <div class="wordmark"><span class="wordmark__dot"></span>Alpine Counsel</div>
</section>

<section class="card card--back" aria-label="Card back">
  <svg class="card__shape" viewBox="0 0 700 400" aria-hidden="true">
    <rect width="700" height="400" fill="var(--brand-red)"/>
    <ellipse cx="360" cy="215" rx="318" ry="300" fill="var(--arc-grey)" transform="rotate(-8 360 215)"/>
    <ellipse cx="366" cy="210" rx="312" ry="298" fill="var(--paper)" transform="rotate(-8 366 210)"/>
  </svg>

  <div class="wordmark"><span class="wordmark__dot"></span>Alpine Counsel</div>

  <div class="holder">
    <p class="holder__name">Daniel Hart</p>
    <p class="holder__role">President</p>
    <ul class="contact">
      <li class="contact__item">
        <svg class="contact__icon" viewBox="0 0 16 16" aria-hidden="true"><path fill="var(--brand-red)" d="M3.5 1l3 3-1.8 2c.9 1.9 2.4 3.4 4.3 4.3l2-1.8 3 3-2 2.5C6.5 13.5 2.5 9.5 1 3.5z"/></svg>
        555-014-2760
      </li>
      <li class="contact__item">
        <svg class="contact__icon" viewBox="0 0 16 16" aria-hidden="true"><rect x="1" y="3" width="14" height="10" fill="var(--brand-red)"/><path d="M1.5 3.5L8 9l6.5-5.5" fill="none" stroke="#fff" stroke-width="1.4"/></svg>
        info@alpinecounsel.com
      </li>
      <li class="contact__item">
        <svg class="contact__icon" viewBox="0 0 16 16" aria-hidden="true"><circle cx="8" cy="8" r="7" fill="var(--brand-red)"/><path d="M1.5 8h13M8 1.2c-2.5 3.6-2.5 10 0 13.6M8 1.2c2.5 3.6 2.5 10 0 13.6" fill="none" stroke="#fff" stroke-width="1"/></svg>
        www.alpinecounsel.com
      </li>
    </ul>
  </div>
</section>

</body>
</html>
```